New Design for Water Vending Machine

Re-design graphics for face plate of water jug vending machine.

Attached are the following:
-Picture of the current face plate for the vending machine. The layout and workflow of the system have been changed.
-Picture of the new face plate without a decal installed.
-Picture of an actual installation of these vending machines for reference.
-DXF File with layout of the face plate
-PDF File with layout notes

The graphics will be printed on a lexan decal. There will be holes cutout for the following:
-Corvel Credit card reader
-Coin reject button
-Coin slot
-4 x Buttons
-Change return
Each of the cutouts should be approximately 5mm larger in all directions than the cutout size on the DXF file.

The flow of the system is as follows:
1. Insert Coins or tap Paymora/Credit/PrePaid Card
2. Press 'Format' button until desired bottle size is displayed.
3. Press 'Start' to begin filling.
'Pause' Button may be pressed during fill to switch containers or temporarily pause fill.
A poster has also been attached that is currently displayed above the prototype machines for customer reference.

Note that the bottom button is not currently used. Perhaps the design could include a window of sorts to add a label to it down the road.

The logos for TallyPay, Quova and Paymora Swift could be displayed near the cutout for the Corvel system.

The phrase 'Premium Drinking Water processed by Reverse Osmosis' should be displayed somewhere on the plate.

Dimensions of the face plate are 12.75" wide x 29.75" high. Dimensions of the graphics will be 10.25" x 27".

The display window will simply be clear lexan. No material will be cutout. Buffer space around display window should be 7mm.

Requirements
Must have
• Vibrant colors, and be eye catching. We want customers to be visually appealed by the machine. It should also follow a blue color theme. Text needs to be clearly layed out, and be concise.

```html
<!DOCTYPE html>
<html lang="en">
<head>
<meta charset="utf-8">
<title>Water Vending Face Plate</title>
<link href="https://fonts.googleapis.com/css2?family=Arimo:ital,wght@0,400;0,700;1,700&display=swap" rel="stylesheet">
<style>
  :root {
    --page: #ffffff;
    --water-top: #dff4f7;
    --water-mid: #6aaec3;
    --water-deep: #15718f;
    --panel: #217f9e;
    --panel-soft: rgba(33, 127, 158, 0.35);
    --frame: #2a7f9c;
    --cutout: #ffffff;
    --guide: #e01e25;
    --ink: #ffffff;
  }
  * { margin: 0; padding: 0; box-sizing: border-box; }
  html, body { width: 672px; height: 1200px; overflow: hidden; background: var(--page); }
  body { position: relative; font-family: "Arimo", Arial, sans-serif; color: var(--ink); }

  .face-plate {
    position: absolute; left: 125px; top: 54px; width: 409px; height: 1081px;
    border-radius: 6px; overflow: hidden;
    background: linear-gradient(180deg, var(--water-top) 0%, #a9d6e0 22%, var(--water-mid) 48%, #2a83a1 66%, var(--water-deep) 78%, var(--water-deep) 100%);
  }
  .bubble-field { position: absolute; inset: 0; background: radial-gradient(circle at 30% 40%, rgba(255,255,255,0.18), transparent 60%); }
  .abs { position: absolute; }

  .display-window {
    left: 81px; top: 9px; width: 249px; height: 50px;
    border: 7px solid var(--frame); border-radius: 9px; background: var(--cutout);
  }

  .coin-reject { left: 96px; top: 130px; width: 30px; height: 30px; border-radius: 50%; background: var(--cutout); }
  .coin-reject::after { content: ""; position: absolute; left: 7px; top: 7px; width: 16px; height: 16px; border: 1.5px solid var(--guide); border-radius: 50%; }
  .coin-slot { left: 128px; top: 114px; width: 19px; height: 62px; border-radius: 8px; background: var(--cutout); }
  .coin-slot::after { content: ""; position: absolute; left: 6px; top: 7px; width: 7px; height: 48px; border: 1.5px solid var(--guide); border-radius: 4px; }

  .step-panel { background: var(--panel); display: flex; align-items: center; }
  .step-number { font-weight: 700; line-height: 1; }
  .step-one { left: 24px; top: 189px; width: 221px; height: 62px; }
  .step-one .step-number { font-size: 48px; width: 42px; text-align: center; margin-left: 3px; }
  .step-one .step-title { font-size: 10.5px; font-weight: 700; line-height: 12.5px; }
  .step-one .step-note { font-size: 8px; font-weight: 700; line-height: 10px; margin-top: 2px; }

  .card-reader { left: 255px; top: 111px; width: 149px; height: 182px; border-radius: 9px; background: var(--cutout); }
  .card-reader::after { content: ""; position: absolute; left: 7px; top: 7px; right: 7px; bottom: 7px; border: 1.5px solid var(--guide); }

  .payment-panel { left: 254px; top: 299px; width: 150px; height: 54px; background: var(--panel); text-align: center; padding-top: 6px; }
  .payment-names { display: flex; justify-content: center; gap: 3px; margin-bottom: 5px; }
  .payment-name { font-size: 7px; font-weight: 700; background: rgba(255,255,255,0.18); padding: 3px 3px; }
  .payment-note { font-size: 8px; font-weight: 700; line-height: 10px; }

  .step-two, .step-three, .step-pause { left: 143px; width: 223px; height: 61px; }
  .step-two { top: 398px; }
  .step-three { top: 518px; }
  .step-pause { top: 638px; background: var(--panel-soft); }
  .step-two .step-number, .step-three .step-number { font-size: 46px; margin-left: 15px; }
  .step-label { position: absolute; right: 77px; text-align: right; font-weight: 700; }
  .step-label .label-main { font-size: 21px; line-height: 22px; }
  .step-label .label-note { font-size: 8.5px; line-height: 10px; }
  .step-two .step-label { top: 8px; }
  .step-three .step-label, .step-pause .step-label { top: 18px; font-size: 21px; }

  .button-cutout { width: 55px; height: 55px; border-radius: 50%; background: var(--cutout); left: 302px; }
  .button-cutout::after { content: ""; position: absolute; left: 7px; top: 7px; width: 41px; height: 41px; border: 1.5px solid var(--guide); border-radius: 50%; box-sizing: border-box; }
  .button-format { top: 401px; }
  .button-start { top: 521px; }
  .button-pause { top: 641px; }
  .button-spare { top: 761px; }

  .tagline { left: 0; width: 409px; text-align: center; font-weight: 700; font-style: italic; }
  .tagline-main { top: 852px; font-size: 29px; }
  .tagline-sub { top: 892px; font-size: 19.5px; }

  .change-return { left: 25px; top: 945px; width: 143px; height: 75px; border-radius: 8px; background: var(--cutout); }
  .change-return::after { content: ""; position: absolute; left: 7px; top: 7px; right: 7px; bottom: 7px; border: 1.5px solid var(--guide); border-radius: 3px; }
</style>
</head>
<body>
<main class="face-plate">
  <div class="bubble-field" role="img" aria-label="Background of rising water bubbles"></div>

  <div class="abs display-window" aria-label="Display window"></div>
  <div class="abs coin-reject" aria-label="Coin reject button"></div>
  <div class="abs coin-slot" aria-label="Coin slot"></div>

  <section class="abs step-panel step-one">
    <span class="step-number">1</span>
    <div>
      <p class="step-title">Insert Coins or tap<br>Paymora/Credit/PrePaid Card</p>
      <p class="step-note">Machine will provide change when bottle<br>size is selected, and start button is pressed</p>
    </div>
  </section>

  <div class="abs card-reader" aria-label="Corvel card reader"></div>

  <section class="abs payment-panel">
    <div class="payment-names">
      <span class="payment-name">TallyPay</span>
      <span class="payment-name">Quova</span>
      <span class="payment-name">Paymora Swift</span>
    </div>
    <p class="payment-note">Credit/Paymora and coin<br>combinations not accepted</p>
  </section>

  <section class="abs step-panel step-two">
    <span class="step-number">2</span>
    <div class="step-label">
      <p class="label-main">Format</p>
      <p class="label-note">Press until desired<br>bottle size is displayed</p>
    </div>
  </section>
  <div class="abs button-cutout button-format" aria-label="Format button"></div>

  <section class="abs step-panel step-three">
    <span class="step-number">3</span>
    <p class="step-label">Start</p>
  </section>
  <div class="abs button-cutout button-start" aria-label="Start button"></div>

  <section class="abs step-panel step-pause">
    <p class="step-label">Pause</p>
  </section>
  <div class="abs button-cutout button-pause" aria-label="Pause button"></div>

  <div class="abs button-cutout button-spare" aria-label="Spare button"></div>

  <h1 class="abs tagline tagline-main">Premium Drinking Water</h1>
  <p class="abs tagline tagline-sub">Processed by Reverse Osmosis</p>

  <div class="abs change-return" aria-label="Change return"></div>
</main>
</body>
</html>
```